Wren Hollow Oils - Body Oils

I am in need of 4 different label and package designs for a new line of body oils that I am launching. I already have the logo and names, it is now a matter of positioning the content. The names are as follows;

1) CARDAMOM + CYPRESS
WARMING BODY OIL
2) NEROLI + LEMON
UPLIFTING BODY OIL
3) CEDAR + BIRCH
GROUNDING BODY OIL
4) SAGE + MINT
COOLING BODY OIL.
The size of each label is 13cm wide x 9.5cm high. The size of the box is 4.5cm x 4.5cm x 15.5cm high.
The size of the bottle is 4cm across the base and 10.5cm in glass height.
I have included an image from a line that I started to work on but it didn't go anywhere. I thought the borders looked good to frame it in however, I am not attached to anything at this point. I am also including a picture of a product line that has used different colors on the packaging. I am not certain that this is the direction I'd like to take however I like how it looks with them. If we were to add the color I think it should be JUST the boxes and NOT the labels and they would be as follows; WARMING OIL - warm burgundy, earth tones UPLIFTING OIL - warm light, lightish blues GROUNDING OIL - warm soft, brownish creams COOLING OIL - refreshing light, pale green possibly blue. I would be interested to see what adding a sprig of a plant would look like on the boxes however with the already busy logo it might look like too much is going on. As you will see in our instagram and website we currently have the bear logo in a foil. I am not sure that I want to proceed with this foil as it is difficult to photograph. I would like to look at colors that compliment the existing line of essential oils as well as the dark brown wood on the cap.
I have added a design that looks a bit industrial that I like, it reads black ops.

Target Market(s)

My market is mainly females who are interested in natural health age 17 - 70. There is a large movement for organic + green beauty. I would like the label to look and feel clean and natural. Something that has been wildcrafted, raw and completely from nature.

Industry/Entity Type

Health And Wellness

Colors

Designer to choose colors to be used in the design.

Requirements
Must have
• Appeal to very progressive organic consumers. Please see the pictures marked SAMPLES 1, 2, 3 + 4 for design ideas.
• Easy to read. Clean design.
• The following information should be on the label as well as the packaging box.
• Size - 100 ML
• Barcodes - still to come
• Ingredients:
• 1) CARDAMOM + CYPRESS WARMING BODY OIL - *Sunflower Oil, **Orange, **Cardamom, **Cypress, **Ginger *Organic, **Organic essential oil
• 2) NEROLI + LEMON UPLIFTING BODY OIL - *Sunflower oil, **Orange, **Neroli, **Grapefruit, **Lemon, **Bergamot, **Benzoin, *Organic, **Organic essential oil
• 3) CEDAR + BIRCH GROUNDING BODY OIL - *Sunflower Oil, **Cedarwood, **Birch, **Benzoin, **Patchouli,*Organic, **Organic essential oil
• 4) SAGE + MINT COOLING BODY OIL - *Sunflower oil, **Spearmint, **Clary Sage, **Geranium, **Ylang Ylang, *Organic, **Organic essential oil
• Suggested Use:
• Warm oil if desired. Apply to the full body after bathing, massage in motions toward the heart until the oil is mostly absorbed. Can also be added to bath water.
Nice to have
• I would like to see the designs on the actual bottle (pic included) to see how it looks.
Should not have
• Bright colors.

```html
<!DOCTYPE html>
<html lang="en">
<head>
<meta charset="utf-8">
<title>Wren Hollow Oils – Cardamom + Cypress Warming Body Oil</title>
<link rel="stylesheet" href="https://fonts.googleapis.com/css2?family=Saira+Condensed:wght@500;600&family=Raleway:wght@200;400&display=swap">
<style>
  :root {
    --burgundy: #a45756;
    --ink: #1e1e1e;
    --paper: #ffffff;
    --frost: #f1f1f1;
    --backdrop: #d6d6d6;
    --rule: #c9c9c9;
  }
  * { box-sizing: border-box; margin: 0; padding: 0; }
  html, body { width: 902px; height: 1200px; overflow: hidden; }
  body { background: var(--backdrop); position: relative; font-family: "Raleway", sans-serif; }

  /* Box dieline panels */
  .box-panel {
    position: absolute;
    top: 170px;
    width: 170px;
    height: 870px;
    background: var(--paper);
    overflow: hidden;
  }
  .box-panel--front { left: 110px; }
  .box-panel--side { left: 280px; border-left: 1px solid var(--rule); }

  .band { position: absolute; left: 0; width: 100%; background: var(--burgundy); }
  .band--top { top: 0; height: 45px; }
  .band--bottom { top: 510px; bottom: 0; display: flex; align-items: center; justify-content: center; }

  /* Vertical product title, read bottom to top */
  .title-line {
    position: absolute;
    writing-mode: vertical-rl;
    transform: rotate(180deg);
    white-space: nowrap;
    line-height: 1;
    text-align: start;
  }
  .title-line--scent {
    font-family: "Saira Condensed", sans-serif;
    font-weight: 600;
    letter-spacing: 0.12em;
  }
  .title-line--type {
    font-family: "Raleway", sans-serif;
    font-weight: 200;
    letter-spacing: 0.01em;
  }

  .box-panel .title-line { top: 120px; height: 340px; }
  .box-panel .title-line--scent { left: 50px; width: 28px; font-size: 24px; font-style: italic; color: var(--burgundy); }
  .box-panel .title-line--type { left: 82px; width: 28px; font-size: 26px; color: var(--ink); }

  .volume {
    position: absolute;
    font-family: "Saira Condensed", sans-serif;
    font-weight: 500;
    letter-spacing: 0.08em;
    color: var(--ink);
    line-height: 1;
  }
  .box-panel .volume { left: 64px; top: 478px; font-size: 13px; }

  .brand-name {
    font-family: "Saira Condensed", sans-serif;
    font-weight: 600;
    letter-spacing: 0.1em;
    text-transform: uppercase;
    text-align: center;
    line-height: 1.2;
  }
  .box-panel .brand-name { font-size: 18px; color: var(--paper); padding: 0 10px; }

  .ingredients { position: absolute; left: 12px; right: 12px; top: 380px; text-align: center; }
  .ingredients__heading {
    font-family: "Saira Condensed", sans-serif;
    font-weight: 500;
    font-size: 12px;
    letter-spacing: 0.12em;
    color: var(--burgundy);
    margin-bottom: 6px;
  }
  .ingredients__list { font-size: 9px; line-height: 1.5; color: var(--ink); font-weight: 400; }

  /* Bottle label */
  .bottle-label {
    position: absolute;
    left: 560px; top: 250px;
    width: 220px; height: 760px;
    background: var(--frost);
    border-radius: 26px 26px 70px 70px;
    overflow: hidden;
  }
  .bottle-label .title-line { top: 110px; height: 300px; }
  .bottle-label .title-line--scent { left: 78px; width: 26px; font-size: 22px; color: var(--ink); }
  .bottle-label .title-line--type { left: 112px; width: 28px; font-size: 24px; color: var(--ink); }
  .bottle-label .brand-name { position: absolute; left: 0; width: 100%; top: 470px; font-size: 18px; color: var(--ink); }
  .bottle-label .volume { left: 0; width: 100%; text-align: center; top: 640px; font-size: 14px; }
</style>
</head>
<body>

  <section class="box-panel box-panel--front" aria-label="Box front panel">
    <div class="band band--top"></div>
    <h1 class="title-line title-line--scent">CARDAMOM + CYPRESS</h1>
    <p class="title-line title-line--type">WARMING BODY OIL</p>
    <p class="volume">100ML</p>
    <div class="band band--bottom">
      <p class="brand-name">Wren Hollow Oils</p>
    </div>
  </section>

  <section class="box-panel box-panel--side" aria-label="Box side panel">
    <div class="band band--top"></div>
    <div class="ingredients">
      <h2 class="ingredients__heading">INGREDIENTS:</h2>
      <p class="ingredients__list">*Sunflower Oil, **Orange,<br>**Cardamom, **Cypress, **Ginger<br>*Organic, **Organic essential oil</p>
    </div>
    <div class="band band--bottom"></div>
  </section>

  <section class="bottle-label" aria-label="Bottle label">
    <h2 class="title-line title-line--scent">CARDAMOM + CYPRESS</h2>
    <p class="title-line title-line--type">WARMING BODY OIL</p>
    <p class="brand-name">Wren Hollow Oils</p>
    <p class="volume">100ML</p>
  </section>

</body>
</html>
```